Adventurous female pilot

I am looking for a personal business card, for a very well qualified female pilot, with a lot of aviation experience.

Currently an airline pilot, have worked as a bush pilot in Africa, looking to get into corporate aviation, or private jet owners.
Want a classy looking card for networking...

Could be interested in a retro\vintage look also?!

An idea,, is an african sunset background, with my wings\logo on it
Updates

I just want to say thank you to all of your for your amazing designs!

I have been very busy flying this past week , so not had a chance to be on the computer much.
But I provide some feedback, and conclusions very soon!
Thank you again.

Marla

Reason: Still waiting on a couple of revisions to be 100% about my choice!

Target Market(s)

corporate aviation, private jet owners, casino's,
General audience.
networking

Industry/Entity Type

Airline

Requirements
Nice to have
• Classy, edgy, sexy, but also feminine

```html
<!DOCTYPE html>
<html lang="en">
<head>
<meta charset="utf-8">
<title>Marla Hollis – Aviator Business Card</title>
<link rel="stylesheet" href="https://fonts.googleapis.com/css2?family=Jost:wght@500&family=Source+Sans+3:wght@400&display=swap">
<style>
  :root {
    --page-bg: #f7f8f8;
    --card-bg: #ffffff;
    --card-edge: #e6e8e8;
    --frame: #1a1a1a;
    --ink: #111111;
    --label: #8a8a8a;
    --wing-light: #e4e4e4;
    --wing-mid: #b9b9b9;
  }
  html, body {
    margin: 0;
    padding: 0;
    width: 1000px;
    height: 1200px;
    overflow: hidden;
    background: var(--page-bg);
  }
  .canvas {
    position: relative;
    width: 1000px;
    height: 1200px;
  }
  .business-card {
    position: absolute;
    left: 198px;
    top: 75px;
    width: 600px;
    height: 1050px;
    background: var(--card-bg);
    box-shadow: 0 0 0 1px var(--card-edge);
  }
  .card-frame {
    position: absolute;
    left: 20px;
    top: 20px;
    width: 556px;
    height: 1006px;
    border: 2px solid var(--frame);
  }
  .card-frame::after {
    content: "";
    position: absolute;
    inset: 3px;
    border: 1px solid var(--frame);
  }
  .wings-emblem {
    position: absolute;
    left: 80px;
    top: 70px;
    width: 442px;
    height: 150px;
    background: radial-gradient(ellipse at center, var(--wing-mid) 0%, var(--wing-light) 60%, var(--card-bg) 100%);
  }
  .identity {
    position: absolute;
    left: 0;
    top: 258px;
    width: 600px;
    text-align: center;
    font-family: "Jost", "Futura", sans-serif;
    font-weight: 500;
    color: var(--ink);
  }
  .identity .full-name {
    margin: 0;
    font-size: 66px;
    line-height: 1;
    letter-spacing: 1px;
  }
  .identity .role {
    margin: 30px 0 0;
    font-size: 32px;
    line-height: 1;
    letter-spacing: 1.5px;
  }
  .contact-list {
    position: absolute;
    left: 39px;
    top: 695px;
    margin: 0;
    font-family: "Source Sans 3", "Myriad Pro", sans-serif;
  }
  .contact-list dt {
    font-size: 25px;
    color: var(--label);
    line-height: 1;
    letter-spacing: 0.5px;
  }
  .contact-list dd {
    margin: 14px 0 38px;
    font-size: 34px;
    color: var(--ink);
    line-height: 1;
  }
  .contact-list dd:last-child { margin-bottom: 0; }
</style>
</head>
<body>
  <div class="canvas">
    <article class="business-card">
      <div class="card-frame"></div>
      <div class="wings-emblem" role="img" aria-label="Pilot wings emblem with a winged horse head"></div>
      <header class="identity">
        <h1 class="full-name">MARLA HOLLIS</h1>
        <p class="role">AVIATOR</p>
      </header>
      <dl class="contact-list">
        <dt>CELL US:</dt>
        <dd>+1 555-014-2768</dd>
        <dt>CELL TAIPEI:</dt>
        <dd>+886 900-555-314</dd>
        <dt>EMAIL:</dt>
        <dd>marlachollis@skymail.net</dd>
      </dl>
    </article>
  </div>
</body>
</html>
```